Boutique custom software development company needs new business card

Our nearly 20 year old custom software development company would like to better include the fact that we are now providing Bitcoin services. These new services are B2B include education (how to acquire and securely hold Bitcoin) and integrating Bitcoin payments into existing ecommerce sites or other existing systems. Please keep the card clean and simple. Attached is our current design and some other files. vexalon.example

Target Market(s)

businesses owners interested in long term relationship

Industry/Entity Type

Custom software development and Bitcoin

Contact Information for Business Card

Marcus Ellwood, marcus@vexalon.example, vexalon.example, (888) 555-VEXAL

Font styles to use
Other font styles liked:
• monospace

Requirements
Must have
• double-sided
Nice to have
• clean and simple
Should not have
• physical address

```html
<!DOCTYPE html>
<html lang="en">
<head>
<meta charset="utf-8">
<title>Vexalon Business Card</title>
<link rel="stylesheet" href="https://fonts.googleapis.com/css2?family=Lato:wght@400&family=Montserrat:wght@400;500;600;700&display=swap">
<style>
  :root {
    --brand-blue: #3e71b8;
    --brand-orange: #f07c22;
    --ink: #444444;
    --card: #ffffff;
    --backdrop: #111111;
  }
  * { box-sizing: border-box; margin: 0; padding: 0; }
  html, body {
    width: 1200px; height: 848px; overflow: hidden;
    background: var(--backdrop);
  }
  .canvas { position: relative; width: 1200px; height: 848px; }
  .card {
    position: absolute; left: 281px; width: 615px; height: 334px;
    background: var(--card);
  }
  .card--front { top: 68px; }
  .card--back { top: 445px; }
  .row {
    position: absolute; left: 0; right: 0;
    display: flex; justify-content: center; align-items: center;
    transform: translateY(-50%);
    white-space: nowrap;
  }
  .wordmark {
    top: 152px;
    font-family: "Montserrat", sans-serif; font-weight: 700;
    font-size: 58px; letter-spacing: 1px; color: var(--brand-blue);
  }
  .tagline {
    top: 199px;
    font-family: "Lato", sans-serif; font-size: 21px;
    letter-spacing: -0.6px; color: var(--brand-blue);
  }
  .services {
    top: 234px; gap: 8px;
    font-family: "Montserrat", sans-serif; font-weight: 500;
    font-size: 12px; letter-spacing: 1.5px; text-transform: uppercase;
    color: var(--brand-orange);
  }
  .services .dot {
    width: 4px; height: 4px; border-radius: 50%; background: var(--brand-orange);
  }
  .front-url {
    top: 298px;
    font-family: "Montserrat", sans-serif; font-weight: 500;
    font-size: 13px; color: var(--ink);
  }
  .back-mark {
    top: 95px; gap: 12px;
    font-family: "Montserrat", sans-serif; font-weight: 700;
    font-size: 34px; color: var(--brand-blue);
  }
  .back-mark .mark-square {
    width: 30px; height: 30px; background: var(--brand-blue);
  }
  .person-name {
    top: 251px;
    font-family: "Montserrat", sans-serif; font-weight: 600;
    font-size: 23px; color: var(--brand-blue);
  }
  .name-rule {
    position: absolute; top: 268px; left: 302px;
    width: 11px; height: 2px; background: var(--brand-blue);
  }
  .contacts {
    top: 297px; gap: 9px;
    font-family: "Montserrat", sans-serif; font-weight: 400;
    font-size: 13.5px; color: var(--ink);
  }
  .contact { display: flex; align-items: center; gap: 4px; }
  .contact svg { width: 12px; height: 12px; fill: none; stroke: var(--brand-orange); stroke-width: 2; }
</style>
</head>
<body>
<main class="canvas">
  <section class="card card--front">
    <div class="row wordmark">VEXALON</div>
    <div class="row tagline">developer of custom applications</div>
    <div class="row services">
      <span>Bitcoin education</span><span class="dot"></span><span>Bitcoin payment integration</span>
    </div>
    <div class="row front-url">vexalon.example</div>
  </section>

  <section class="card card--back">
    <div class="row back-mark"><span class="mark-square"></span>VEXALON</div>
    <div class="row person-name">Marcus Ellwood</div>
    <span class="name-rule"></span>
    <div class="row contacts">
      <span class="contact">
        <svg viewBox="0 0 24 24" aria-hidden="true"><path d="M5 3h4l2 5-3 2a11 11 0 0 0 6 6l2-3 5 2v4a2 2 0 0 1-2 2A17 17 0 0 1 3 5a2 2 0 0 1 2-2z"/></svg>
        (888) 555-VEXAL
      </span>
      <span class="contact">
        <svg viewBox="0 0 24 24" aria-hidden="true"><rect x="2" y="5" width="20" height="14"/><path d="M2 5l10 8 10-8"/></svg>
        marcus@vexalon.example
      </span>
      <span class="contact">
        <svg viewBox="0 0 24 24" aria-hidden="true"><circle cx="12" cy="12" r="10"/><path d="M2 12h20M12 2c3 3 3 17 0 20M12 2c-3 3-3 17 0 20"/></svg>
        vexalon.example
      </span>
    </div>
  </section>
</main>
</body>
</html>
```